Our New Website is Now Live!

New website launch, with ability to place orders and save quotes online. Our previous website was resource oriented – www.quellvalvekits.com – and new website will be up to date, more interactive, more modern and have all and more repair resources. Company colors are in logo below and throughout new website – https://staging.tidegatefixers.com/. We have always offered free technical phone support and we now will have the ability to chat live on the website with our team for customer service, technical support and any issues.

Target Market(s)

blue collar, 40-60 year old blue collar workers. Message needs to be clear and most people that will see this flyer are not familiar with our old website

Requirements
Must have
• new website launch, repair help, technical assistance
Nice to have
• online chat, pictures from website of product

```html
<!DOCTYPE html>
<html lang="en">
<head>
<meta charset="utf-8">
<title>Our New Website is Now Live!</title>
<link rel="stylesheet" href="https://fonts.googleapis.com/css2?family=Lato:ital,wght@0,400;0,700;0,900;1,400;1,700&display=swap">
<style>
  :root {
    --red: #e8174a;
    --blue: #27399a;
    --navy: #1f2f86;
    --ink: #222;
    --paper: #ffffff;
    --backdrop: #8e8e8e;
    --wood-dark: #5a3a22;
    --wood: #9a7048;
    --wood-light: #c9a57c;
    --silver: #d9dbde;
    --screen: #eef0f4;
  }
  * { margin: 0; padding: 0; box-sizing: border-box; }
  html, body { width: 682px; height: 1200px; overflow: hidden; }
  body { background: var(--backdrop); font-family: "Lato", sans-serif; position: relative; }
  .flyer {
    position: absolute; left: 0; top: 118px; width: 682px; height: 963px;
    background: var(--paper); overflow: hidden;
    box-shadow: 0 10px 30px rgba(0,0,0,.35);
  }
  .abs { position: absolute; }

  .brand { left: 22px; top: 22px; display: flex; align-items: center; gap: 10px; }
  .brand-mark { width: 26px; height: 26px; background: var(--blue); }
  .brand-name { color: var(--blue); font-size: 22px; font-weight: 400; line-height: 1; }
  .brand-sub { color: var(--blue); font-size: 11px; margin-top: 2px; }

  .hero-photo {
    left: 0; top: 0; width: 682px; height: 500px;
    background:
      radial-gradient(ellipse 150px 110px at 590px 505px, rgba(255,255,255,.9), rgba(255,255,255,0) 70%),
      radial-gradient(ellipse 175px 120px at 470px 225px, var(--screen) 0%, #c7ccd6 55%, rgba(120,124,132,0) 75%),
      radial-gradient(ellipse 230px 95px at 470px 360px, #e9eaec 0%, var(--silver) 45%, rgba(150,152,158,0) 80%),
      linear-gradient(90deg, rgba(240,240,238,.92) 0%, rgba(235,233,228,.75) 28%, rgba(235,233,228,0) 48%),
      radial-gradient(ellipse 260px 120px at 80px 110px, #5f7a4c 0%, rgba(95,122,76,0) 80%),
      linear-gradient(180deg, rgba(255,255,255,0) 60%, rgba(248,248,248,.85) 100%),
      linear-gradient(125deg, var(--wood-light) 0%, var(--wood) 35%, var(--wood-dark) 60%, var(--wood) 80%, var(--wood-light) 100%);
    clip-path: polygon(0 90px, 275px 90px, 325px 46px, 682px 46px, 682px 450px, 605px 450px, 560px 492px, 0 492px);
  }
  .headline {
    left: 27px; top: 198px; color: var(--red); font-weight: 900;
    font-size: 40px; line-height: 49px; letter-spacing: -.3px;
    text-shadow: 0 1px 4px rgba(255,255,255,.9);
  }
  .hero-url { left: 21px; top: 366px; color: var(--blue); font-weight: 700; font-size: 15px; }

  .tagline { left: 0; width: 682px; top: 528px; text-align: center; color: var(--red); font-style: italic; font-size: 17px; }
  .section-label {
    left: 262px; top: 571px; width: 160px; height: 27px; background: var(--blue);
    color: #fff; font-size: 17px; text-align: center; line-height: 27px;
  }

  .product { top: 618px; width: 206px; height: 138px; }
  .product-frame {
    position: absolute; left: 6px; right: 6px; top: 14px; bottom: 6px; border: 3px solid var(--red);
    transform: skewX(-8deg); background: #fff;
  }
  .product-photo {
    position: absolute; left: 30px; right: 30px; top: 48px; height: 56px;
    background: linear-gradient(90deg, #8a6a3c, #c8a069, #6b7a4c, #b08a55, #8a6a3c);
    border-radius: 8px;
  }
  .product-photo.steel { background: linear-gradient(90deg, #8b8f95, #d7d9dc, #7c8086, #c4c7cb, #8b8f95); }
  .product-photo.dark { background: linear-gradient(90deg, #b08a55, #2a2c33, #3a3d46, #2a2c33, #b08a55); }

  .note {
    left: 60px; width: 562px; top: 782px; text-align: center; color: var(--ink);
    font-size: 13.5px; line-height: 17px;
  }
  .chat-label { left: 172px; top: 848px; font-size: 13px; font-weight: 700; color: var(--ink); }
  .contact { left: 14px; display: flex; align-items: center; gap: 9px; color: var(--blue); }
  .contact.phone { top: 888px; font-size: 21px; }
  .contact.web { top: 926px; font-size: 13px; color: var(--ink); }
  .chat-art {
    left: 243px; top: 852px; width: 100px; height: 105px;
    background: linear-gradient(160deg, #f28a5a, #7cc6a8 45%, #f3c98b 80%);
    border-radius: 8px; opacity: .9;
  }
  .assist {
    left: 346px; top: 842px; width: 219px; height: 115px; background: var(--navy);
    color: #fff; padding: 12px 10px 0 34px;
    clip-path: polygon(22px 0, 100% 0, 100% 100%, 0 100%);
  }
  .assist h2 { font-size: 14px; font-weight: 700; margin-bottom: 6px; }
  .assist li { list-style: none; font-size: 11px; line-height: 14px; }
  .valve-photo {
    left: 565px; top: 842px; width: 117px; height: 115px;
    background: linear-gradient(135deg, #d9d4cf, #c7756a 45%, #8e8f92 70%, #e7e2dc);
  }
  .bottom-bar { left: 0; top: 957px; width: 682px; height: 6px; background: var(--red); }
  .lines { left: 0; top: 0; }
</style>
</head>
<body>
<main class="flyer">
  <div class="abs hero-photo" role="img" aria-label="Photo of a laptop showing the new website's home page with valve parts, on a wooden table beside a tablet, glasses and a coffee cup"></div>

  <svg class="abs lines" width="682" height="963" viewBox="0 0 682 963" aria-hidden="true">
    <g fill="none" stroke-width="3">
      <polyline points="0,80 268,80 318,36 594,36" stroke="var(--red)"/>
      <polyline points="0,88 274,88 324,44 682,44" stroke="var(--blue)"/>
      <polyline points="0,496 556,496 602,454 682,454" stroke="var(--red)"/>
      <polyline points="180,504 562,504 608,462 682,462" stroke="var(--blue)"/>
    </g>
    <circle cx="597" cy="36" r="4" fill="var(--red)"/>
    <circle cx="180" cy="504" r="4" fill="var(--blue)"/>
    <g fill="none" stroke="var(--blue)" stroke-width="2.5">
      <polyline points="58,636 38,636 22,740"/>
      <polyline points="200,758 218,758 232,660"/>
      <polyline points="270,636 250,636 234,740"/>
      <polyline points="412,758 430,758 444,660"/>
      <polyline points="480,636 460,636 444,740"/>
      <polyline points="622,758 640,758 654,660"/>
    </g>
    <g fill="none" stroke-width="2.5">
      <polyline points="0,846 150,846 172,868" stroke="var(--blue)"/>
      <polyline points="150,838 340,838" stroke="var(--red)"/>
      <polyline points="150,838 126,866 0,866" stroke="var(--red)"/>
    </g>
  </svg>

  <div class="abs brand">
    <div class="brand-mark"></div>
    <div>
      <div class="brand-name">Harbor Valve Supply Co.</div>
    </div>
  </div>

  <h1 class="abs headline">Our<br>New Website<br>is Now Live!</h1>
  <div class="abs hero-url">https://staging.tidegatefixers.com</div>

  <p class="abs tagline">New website launch, with ability to place orders and save quotes online.</p>
  <div class="abs section-label">Our Repair Parts</div>

  <div class="abs product" style="left:26px">
    <div class="product-frame"></div>
    <div class="product-photo" role="img" aria-label="Bronze backflow valve assembly"></div>
  </div>
  <div class="abs product" style="left:238px">
    <div class="product-frame"></div>
    <div class="product-photo steel" role="img" aria-label="Stainless steel backflow preventer"></div>
  </div>
  <div class="abs product" style="left:448px">
    <div class="product-frame"></div>
    <div class="product-photo dark" role="img" aria-label="Black backflow valve with bronze fittings"></div>
  </div>

  <p class="abs note">We have always offered free technical phone support and we now will have the ability<br>to chat live on the website with our team for customer service</p>

  <div class="abs chat-label">Online Chat</div>
  <div class="abs contact phone">
    <svg width="18" height="18" viewBox="0 0 24 24" fill="none" stroke="var(--blue)" stroke-width="2"><circle cx="12" cy="12" r="10.5"/><path d="M8 7l2 0 1 3-1.5 1a7 7 0 003.5 3.5l1-1.5 3 1v2c0 .6-.5 1-1 1A10 10 0 017 8c0-.5.4-1 1-1z" fill="var(--blue)" stroke="none"/></svg>
    <span>(800) 555-0142</span>
  </div>
  <div class="abs contact web">
    <svg width="15" height="15" viewBox="0 0 24 24" fill="none" stroke="var(--blue)" stroke-width="2"><circle cx="12" cy="12" r="10"/><path d="M2 12h20M12 2c3 3 3 17 0 20M12 2c-3 3-3 17 0 20"/></svg>
    <span>staging.tidegatefixers.com</span>
  </div>
  <div class="abs chat-art" role="img" aria-label="Illustration of hands holding a phone with chat bubbles"></div>

  <section class="abs assist">
    <h2>Technical Assistance</h2>
    <ul>
      <li>Free Phone Tech Assistance</li>
      <li>Live Chat Tech Assistance</li>
      <li>Experienced Technicians On Staff</li>
      <li>Step-By-Step Repair Instructions</li>
      <li>Repair Videos</li>
    </ul>
  </section>
  <div class="abs valve-photo" role="img" aria-label="Close-up photo of a valve being repaired by hand"></div>
  <div class="abs bottom-bar"></div>
</main>
</body>
</html>
```